Dean Hollis Business Card

In addition to my name design (file uploaded), black print on white card stock, e-mail address should be presented as a typical e-mail address, i.e., underlined and in blue ink, the card should include the following information:
Professor of Aviation Technology
Accident Litigation Expert Witness
Master Certificated Flight Instructor

dhollis@vexmail.example
Anchorage, Alaska
(907) 318-5074

```html
<!DOCTYPE html>
<html lang="en">
<head>
<meta charset="utf-8">
<title>Dean Hollis — Business Card</title>
<link rel="stylesheet" href="https://fonts.googleapis.com/css2?family=Archivo+Narrow:wght@400&family=Oswald:wght@600&display=swap">
<style>
  :root {
    --card-bg: #ffffff;
    --ink: #111111;
    --muted-ink: #5f6b6d;
    --link-blue: #1b1bf0;
  }
  html, body {
    margin: 0;
    padding: 0;
    width: 1200px;
    height: 720px;
    overflow: hidden;
    background: var(--card-bg);
  }
  .card {
    position: relative;
    width: 1200px;
    height: 720px;
    background: var(--card-bg);
    color: var(--ink);
  }
  .card-column {
    position: absolute;
    left: 0;
    width: 1176px;
    text-align: center;
  }
  .name-mark {
    top: 152px;
    margin: 0;
    font-family: "Oswald", "Arial Narrow", sans-serif;
    font-weight: 600;
    font-size: 66px;
    line-height: 1;
    letter-spacing: 0.5px;
    color: var(--ink);
    text-transform: uppercase;
  }
  .credentials {
    top: 294px;
    margin: 0;
    padding: 0;
    list-style: none;
    font-family: "Archivo Narrow", "Arial Narrow", sans-serif;
    font-weight: 400;
    font-size: 33px;
    line-height: 44px;
    letter-spacing: 1.6px;
    color: var(--ink);
  }
  .contact-line {
    top: 552px;
    margin: 0;
    font-family: "Archivo Narrow", "Arial Narrow", sans-serif;
    font-weight: 400;
    font-size: 29px;
    line-height: 40px;
    letter-spacing: 1.4px;
    color: var(--muted-ink);
  }
  .contact-email {
    color: var(--link-blue);
    text-decoration: underline;
    text-decoration-thickness: 1px;
    text-underline-offset: 5px;
  }
  .contact-divider {
    display: inline-block;
    margin: 0 26px;
  }
</style>
</head>
<body>
  <main class="card">
    <h1 class="card-column name-mark">Dean E. Hollis</h1>
    <ul class="card-column credentials">
      <li>Professor of Aviation Technology</li>
      <li>Accident Litigation Expert Witness</li>
      <li>Master Certificated Flight Instructor</li>
    </ul>
    <p class="card-column contact-line">
      <a class="contact-email" href="mailto:dhollis@vexmail.example">dhollis@vexmail.example</a><span class="contact-divider">|</span><span class="contact-location">Anchorage, Alaska</span><span class="contact-divider">|</span><span class="contact-phone">(907) 318-5074</span>
    </p>
  </main>
</body>
</html>
```